Mezzanine Floor Manufacturer looking for a new business card design

We manufacture mezzanine floors and are providers of racking systems. We provide a range of items/services - simple rack repairs , full warehouse fit outs , manufacturer and install mezzanine floors , partitioning and large turnkey projects. Recently had a new website - www.corvane-shelving.co.uk and would like our business cards updating aswell . Our current card is single sided in the old logo colours (pdf attached) and needs updating.

Target Market(s)

We deal with large projects/ multi national companies and also smaller projects and companies throughout the UK ranging from a single warehouse to a large multi site company.

Industry/Entity Type

Business

Contact Information for Business Card

Will have job title,tel no's, email ,website address etc like example pdf

Requirements
Must have
• Hi - needs to use the colours of the logo & new website. Card needs to be professional

```html
<!DOCTYPE html>
<html lang="en">
<head>
<meta charset="utf-8">
<title>Business Card – Technical Sales</title>
<link href="https://fonts.googleapis.com/css2?family=Tinos&display=swap" rel="stylesheet">
<style>
  :root {
    --page-bg: #ffffff;
    --panel-dark: #333333;
    --panel-dark-2: #3a3a3a;
    --accent-red: #d40000;
    --name-white: #ffffff;
    --role-grey: #a6a6a6;
    --service-gold: #f0c419;
    --ink: #111111;
  }
  html, body {
    margin: 0;
    padding: 0;
    overflow: hidden;
    background: var(--page-bg);
  }
  .card {
    position: relative;
    width: 1200px;
    height: 653px;
    overflow: hidden;
    background: var(--page-bg);
    font-family: "Tinos", "Times New Roman", serif;
  }
  .card__shapes {
    position: absolute;
    inset: 0;
  }
  .card__text {
    position: absolute;
    margin: 0;
    white-space: nowrap;
  }
  .name {
    left: 605px;
    top: 314px;
    font-size: 41px;
    color: var(--name-white);
  }
  .name__surname { color: var(--accent-red); }
  .role {
    left: 649px;
    top: 358px;
    font-size: 33px;
    color: var(--role-grey);
  }
  .services {
    position: absolute;
    left: 682px;
    top: 396px;
    margin: 0;
    padding: 0;
    list-style: none;
    font-size: 19px;
    line-height: 27px;
    color: var(--service-gold);
  }
  .phones {
    font-size: 22px;
    color: var(--ink);
  }
  .phone--mob { left: 953px; top: 362px; }
  .phone--tel { left: 932px; top: 397px; }
  .phone--fax { left: 917px; top: 434px; }
  .address {
    position: absolute;
    left: 898px;
    top: 498px;
    margin: 0;
    font-style: normal;
    font-size: 18.5px;
    line-height: 30.5px;
    color: var(--ink);
  }
</style>
</head>
<body>
<div class="card">
  <svg class="card__shapes" width="1200" height="653" viewBox="0 0 1200 653">
    <defs>
      <linearGradient id="panelShade" x1="0" y1="0" x2="1" y2="1">
        <stop offset="0" stop-color="var(--panel-dark-2)"/>
        <stop offset="1" stop-color="var(--panel-dark)"/>
      </linearGradient>
    </defs>
    <polygon class="panel" points="559,268 969,268 769,653 559,653" fill="url(#panelShade)"/>
    <polygon class="accent-stripe" points="969,268 990,268 797,653 769,653" fill="var(--accent-red)"/>
  </svg>

  <h1 class="card__text name">Daniel <span class="name__surname">Hartley</span></h1>
  <p class="card__text role">Technical Sales</p>

  <ul class="services">
    <li>Mezzanine Floors</li>
    <li>Cantilever Racking</li>
    <li>Safety Barriers</li>
    <li>Partitioning</li>
    <li>Turnkey Projects</li>
    <li>Longspan Selving</li>
    <li>Steel Shelving</li>
  </ul>

  <p class="card__text phones phone--mob">Mob: 07700 900482</p>
  <p class="card__text phones phone--tel">Tel: 01632 960418</p>
  <p class="card__text phones phone--fax">Fax: 01632 960527</p>

  <address class="address">
    Eleven Mill Close<br>
    Aldwick Gate Business Park<br>
    Brampton, Derbyshire DE9 4QX
  </address>
</div>
</body>
</html>
```